Business Cards and Stationery incorporating Logo design
Business Cards and Stationery incorporating Logo design -
Creative Brief
Professional
Daniel P. Halvorsen
Managing Director
418 Corvane Tower 9th Fl. Uniondale, NY 11553
1-555-hdg-cash
dhalvorsen@halvorsendrakeco.example
www.halvorsendrakeco.example

```html
<!DOCTYPE html>
<html lang="en">
<head>
<meta charset="utf-8">
<title>Halvorsen Drake — Stationery</title>
<link href="https://fonts.googleapis.com/css2?family=Libre+Baskerville:wght@400;700&family=Open+Sans:wght@400;600&display=swap" rel="stylesheet">
<style>
  :root {
    --bg: #2a2a2b;
    --green: #1e6b3f;
    --paper: #ffffff;
    --paper-shade: #eef0ee;
    --ink: #333333;
    --muted: #8a8f8b;
    --faint: #e4e9e5;
    --serif: "Libre Baskerville", Georgia, serif;
    --sans: "Open Sans", Arial, sans-serif;
  }
  * { box-sizing: border-box; margin: 0; padding: 0; }
  html, body { width: 1200px; height: 310px; overflow: hidden; background: var(--bg); }
  .canvas { position: relative; width: 1200px; height: 310px; background: var(--bg); font-family: var(--sans); color: var(--ink); }
  .piece { position: absolute; background: var(--paper); box-shadow: 0 2px 6px rgba(0,0,0,.45); overflow: hidden; }

  .brand { display: flex; align-items: center; gap: 5px; white-space: nowrap; }
  .brand-square { width: 14px; height: 14px; background: var(--green); flex: none; }
  .brand-name { font-family: var(--serif); font-weight: 700; font-size: 9px; line-height: 1.05; text-transform: uppercase; color: var(--green); }
  .brand--light .brand-square { background: var(--paper); }
  .brand--light .brand-name { color: var(--paper); }

  .hero-brand { position: absolute; left: 14px; top: 24px; display: flex; gap: 10px; align-items: flex-start; }
  .hero-brand .brand-square { width: 38px; height: 38px; background: var(--paper); }
  .hero-brand .brand-name { font-size: 21px; color: var(--paper); line-height: 1.05; }
  .hero-brand .tagline { font-size: 8px; color: var(--muted); margin-top: 6px; font-family: var(--sans); font-weight: 400; text-transform: none; letter-spacing: .5px; }

  .band-left { position: absolute; left: 0; top: 0; bottom: 0; background: var(--green); }
  .tiny { font-size: 4px; line-height: 1.5; color: var(--muted); }
  .contact { position: absolute; text-align: right; white-space: nowrap; }
  .watermark { position: absolute; background: var(--faint); }

  .card-vertical { left: 18px; top: 128px; width: 96px; height: 104px; }
  .card-vertical .band-left { width: 8px; }
  .card-vertical .brand { position: absolute; left: 15px; top: 12px; }
  .card-vertical .brand-square { width: 11px; height: 11px; }
  .card-vertical .brand-name { font-size: 7px; }
  .card-vertical .person { position: absolute; left: 15px; top: 40px; right: 6px; }
  .person-name { font-size: 5.5px; font-weight: 600; color: var(--ink); margin-bottom: 2px; }

  .card-white { left: 18px; top: 240px; width: 94px; height: 50px; display: flex; align-items: center; justify-content: center; }
  .card-green { left: 118px; top: 240px; width: 94px; height: 50px; background: var(--green); display: flex; align-items: center; justify-content: center; }
  .card-white .brand-name, .card-green .brand-name { font-size: 8px; }
  .card-white .brand-square, .card-green .brand-square { width: 12px; height: 12px; }

  .letterhead { top: 19px; width: 190px; height: 264px; }
  .letterhead .band-left { width: 12px; }
  .letterhead .brand { position: absolute; left: 20px; top: 14px; }
  .letterhead .brand-square { width: 16px; height: 16px; }
  .letterhead .brand-name { font-size: 8px; }
  .letterhead .contact { right: 8px; top: 14px; }
  .letterhead .watermark { left: 72px; top: 96px; width: 56px; height: 56px; }
  .letterhead .footer { position: absolute; left: 20px; right: 8px; bottom: 10px; text-align: center; white-space: nowrap; }
  .lh-one { left: 288px; }
  .lh-two { left: 492px; }

  .slip { left: 696px; width: 168px; }
  .slip .band-left { width: 10px; }
  .slip .brand { position: absolute; left: 18px; top: 10px; }
  .slip .brand-square { width: 12px; height: 12px; }
  .slip .brand-name { font-size: 7.5px; }
  .slip .watermark { right: 20px; width: 32px; height: 32px; }
  .slip-one { top: 24px; height: 110px; }
  .slip-one .watermark { top: 52px; }
  .slip-one .contact { right: 8px; top: 10px; }
  .slip-two { top: 168px; height: 100px; }
  .slip-two .watermark { top: 50px; }
  .slip-two .footer { position: absolute; left: 18px; bottom: 8px; white-space: nowrap; }

  .envelope { position: absolute; left: 888px; width: 288px; height: 80px; box-shadow: 0 2px 6px rgba(0,0,0,.45); }
  .env-back { top: 24px; }
  .env-green { top: 112px; }
  .env-front { top: 200px; }
  .env-front .brand { position: absolute; left: 12px; top: 8px; }
  .env-front .brand-square { width: 12px; height: 12px; }
  .env-front .tiny { position: absolute; left: 29px; top: 26px; white-space: nowrap; }
  .envelope svg { display: block; }
</style>
</head>
<body>
<main class="canvas">

  <div class="hero-brand">
    <span class="brand-square"></span>
    <div class="brand-name">Halvorsen<br>Drake<div class="tagline">Investment Group</div></div>
  </div>

  <section class="piece card-vertical" aria-label="Business card, portrait">
    <div class="band-left"></div>
    <div class="brand"><span class="brand-square"></span><span class="brand-name">Halvorsen<br>Drake</span></div>
    <div class="person">
      <p class="person-name">Daniel P. Halvorsen</p>
      <p class="tiny">Managing Director</p>
      <p class="tiny">418 Corvane Tower 9th Fl. Uniondale, NY 11553</p>
      <p class="tiny">1-555-hdg-cash</p>
      <p class="tiny">dhalvorsen@halvorsendrakeco.example</p>
      <p class="tiny">www.halvorsendrakeco.example</p>
    </div>
  </section>

  <section class="piece card-white" aria-label="Business card front, white">
    <div class="brand"><span class="brand-square"></span><span class="brand-name">Halvorsen<br>Drake</span></div>
  </section>
  <section class="piece card-green" aria-label="Business card front, green">
    <div class="brand brand--light"><span class="brand-square"></span><span class="brand-name">Halvorsen<br>Drake</span></div>
  </section>

  <section class="piece letterhead lh-one" aria-label="Letterhead">
    <div class="band-left"></div>
    <div class="brand"><span class="brand-square"></span><span class="brand-name">Halvorsen<br>Drake</span></div>
    <div class="contact tiny"><p>1-555-hdg-cash</p><p>dhalvorsen@halvorsendrakeco.example</p><p>www.halvorsendrakeco.example</p></div>
    <div class="watermark"></div>
    <p class="footer tiny">418 Corvane Tower 9th Fl. Uniondale, NY 11553 · www.halvorsendrakeco.example</p>
  </section>

  <section class="piece letterhead lh-two" aria-label="Letterhead, second page">
    <div class="band-left"></div>
    <div class="brand"><span class="brand-square"></span><span class="brand-name">Halvorsen<br>Drake</span></div>
    <div class="watermark"></div>
    <p class="footer tiny">418 Corvane Tower 9th Fl. Uniondale, NY 11553 · 1-555-hdg-cash</p>
  </section>

  <section class="piece slip slip-one" aria-label="Compliment slip">
    <div class="band-left"></div>
    <div class="brand"><span class="brand-square"></span><span class="brand-name">Halvorsen<br>Drake</span></div>
    <div class="contact tiny"><p>1-555-hdg-cash</p><p>www.halvorsendrakeco.example</p></div>
    <div class="watermark"></div>
  </section>

  <section class="piece slip slip-two" aria-label="Note card">
    <div class="band-left"></div>
    <div class="brand"><span class="brand-square"></span><span class="brand-name">Halvorsen<br>Drake</span></div>
    <div class="watermark"></div>
    <p class="footer tiny">418 Corvane Tower 9th Fl. Uniondale, NY 11553</p>
  </section>

  <div class="envelope env-back" aria-label="Envelope back">
    <svg width="288" height="80" viewBox="0 0 288 80">
      <rect width="288" height="80" fill="#ffffff"/>
      <polygon points="0,80 144,36 288,80" fill="#eef0ee"/>
      <polygon points="0,0 288,0 144,46" fill="#1f1f20"/>
    </svg>
  </div>

  <div class="envelope env-green" aria-label="Envelope back, green flap">
    <svg width="288" height="80" viewBox="0 0 288 80">
      <rect width="288" height="80" fill="#ffffff"/>
      <polygon points="0,80 144,38 288,80" fill="#eef0ee"/>
      <polygon points="0,0 288,0 144,44" fill="#1e6b3f"/>
    </svg>
  </div>

  <div class="envelope env-front piece" aria-label="Envelope front">
    <div class="brand"><span class="brand-square"></span><span class="brand-name">Halvorsen<br>Drake</span></div>
    <p class="tiny">418 Corvane Tower 9th Fl. Uniondale, NY 11553</p>
  </div>

</main>
</body>
</html>
```